Design for 3.31” x 84” vinyl banner for tradeshow

Hello, I am looking for a design that will be printed on a 33.31” x 84” vinyl banner for my company’s tradeshow booth.

-Design

My vision: I want to give you the full background, because I think it’ll help. We design insulation for electronic tools that go in high temperature oilwells. Interestingly, a lot of the electronic tools that go down these oil wells are also used in geothermal wells. However the electronics would melt in these high temperature geothermal wells if they were not insulated. A lot of companies that make tools for the oil market are trying to re-purpose their existing tools for the geothermal market…..and to do this, they would need our insulation.

So, our sign needs to conveys this message: Trying to enter the geothermal logging market? it's as simple as increasing the temp. rating for your existing tools

This sign will be placed at our company’s booth at an industry tradeshow. The sign needs to have a similar style to our existing signs. I’ve included images of our booth and all of our other signs. This sign doesn’t have to be identical in artistic style, but be fairly similar.

-Art Requirements:

At least 1 Image of RDP logo

I’ve included several different variations. Use your judgement to select the one that you think is most fitting.

Do not use the portion of the logo that says “40 years”. Feel free to crop that out if you would like.

At least 2 images of logging tools. You can select more than 2 if you think that’s necessary. Logging tools are the long metal tubes.

I’ve included several pictures of different logging tools. I would like to see at least 2 pictures of tools on the banner. Please include the image titled “Full, double centarlizer” It could look cool if this picture extended the full length of the banner (just a suggestion). I purchased these images off of picvault.For the second image of the tool, feel free to include whatever tool you think looks best.

-Colors and font: Like I mentioned above, I would like it to look close to the other signs we have at our booth. Please select colors and fonts that will fit with our other signs.

-Other thoughts/suggestions

When most people in our industry think of geothermal, the automatically associate it with extremely high temperatures. I’m open to seeing warmer colors (orange/red) that help convey this idea.

I’m also open to seeing pictures of geothermal power plants, I included an image of this titled “geothermal” that you may use if you like. This is not mandatory, just a suggestion.

-Text: the main text needs to be: “Trying to enter the Geothermal logging market? Ask us about increasing the temperature rating for your existing tools” No other text is required.

Printing/Art specifications:

I’ll be giving the design I receive off art-hive to a local banner printing shop. I’ve included their printing and art guidelines, please take a look at it and let me know if you have any questions. It’s pretty detailed so I hope it provides you with enough information. The design would have to follow the requirements in the two attached word documents.

Target Market(s)

oil and gas professionals

Industry/Entity Type

oil and gas/geothermal

Font styles to use
Other font styles liked:
• Fonts similar the font used on our other tradeshow signs (images attached)

Colors
F0912C
F2A743
F7CA91
FBE8D2
FDF5EE

Requirements
Must have
• -At least 1 Image of RDP logo, At least 2 images of logging tools (1 of these 2 pictures must be image titled "full double centralizer", he main text needs to be: “Trying to enter the Geothermal logging market? Ask us about increasing the temperature rating for your existing tools” , the design must follow the requirements in the printing and art guideline documents I attached.
Nice to have
• please select colors and fonts that will fit with our other signs.

```html
<!DOCTYPE html>
<html lang="en">
<head>
<meta charset="utf-8">
<title>RDP Thermal – Geothermal Banner</title>
<link href="https://fonts.googleapis.com/css2?family=Hind:wght@500;600;700&display=swap" rel="stylesheet">
<style>
  :root {
    --stage: #5e5d5f;
    --paper: #ffffff;
    --paper-shade: #eeeeee;
    --ink: #1b1b1b;
    --orange: #e8731a;
    --dark: #262626;
    --steel-light: #d9dadb;
    --steel-dark: #6f7173;
    --copper: #c98a4a;
  }
  * { margin: 0; padding: 0; box-sizing: border-box; }
  html, body { width: 1200px; height: 1000px; overflow: hidden; }
  body {
    background: var(--stage);
    font-family: "Hind", Arial, sans-serif;
    position: relative;
  }
  .banner {
    position: absolute;
    left: 414px; top: 43px;
    width: 372px; height: 915px;
    background: linear-gradient(180deg, var(--paper) 0%, var(--paper-shade) 60%, var(--paper) 100%);
    box-shadow: 8px 10px 18px rgba(0,0,0,.45);
    overflow: hidden;
  }
  .banner__base { position: absolute; left: 0; top: 0; width: 372px; height: 915px; }
  .brand {
    position: absolute; left: 58px; top: 52px;
    display: flex; align-items: center; gap: 10px;
  }
  .brand__square { width: 78px; height: 78px; background: var(--dark); border-radius: 4px; }
  .brand__name {
    font-weight: 700; font-size: 25px; line-height: 25px; color: var(--ink);
    text-transform: uppercase;
  }
  .headline { position: absolute; left: 0; top: 178px; width: 372px; text-align: center; }
  .headline__lead { font-weight: 700; font-size: 29px; line-height: 34px; color: var(--ink); }
  .headline__key { font-weight: 700; font-size: 31px; line-height: 36px; color: var(--orange); }
  .headline__rule {
    position: absolute; top: 43px; width: 40px; height: 14px;
    background: repeating-linear-gradient(180deg, var(--orange) 0 2px, transparent 2px 6px);
  }
  .headline__rule--left { left: 22px; }
  .headline__rule--right { right: 22px; }
  .tool { position: absolute; border-radius: 6px; }
  .tool--horizontal {
    left: 13px; top: 340px; width: 332px; height: 56px;
    background: linear-gradient(90deg, var(--steel-light), var(--copper) 30%, var(--steel-dark) 60%, var(--copper));
  }
  .tool--centralizer {
    left: 20px; top: 410px; width: 55px; height: 475px;
    background: linear-gradient(180deg, var(--steel-light), var(--steel-dark) 70%, #3f4042);
  }
  .tool--slim {
    left: 95px; top: 410px; width: 28px; height: 465px;
    background: linear-gradient(180deg, var(--steel-light), var(--steel-dark));
  }
  .product { position: absolute; left: 130px; top: 452px; }
  .product__name { font-weight: 700; font-size: 29px; line-height: 33px; color: var(--ink); }
  .product__name--accent { color: var(--orange); }
  .cta {
    position: absolute; left: 130px; top: 547px; width: 212px; height: 52px;
    background: var(--orange); color: var(--paper);
    font-weight: 700; font-size: 45px; line-height: 58px; text-align: center;
  }
  .cta-copy {
    position: absolute; left: 130px; top: 606px; width: 220px;
    font-weight: 500; font-size: 19px; line-height: 21px; color: var(--ink);
  }
  .site {
    position: absolute; left: 130px; top: 700px; width: 213px; height: 33px;
    background: var(--dark); color: var(--paper);
    font-weight: 600; font-size: 18px; line-height: 36px; text-align: center;
  }
</style>
</head>
<body>
  <main class="banner">
    <svg class="banner__base" viewBox="0 0 372 915" aria-hidden="true">
      <polygon points="0,712 372,792 372,915 0,915" fill="#e8731a"/>
      <polygon points="0,703 340,833 245,915 0,915" fill="#262626"/>
    </svg>

    <header class="brand">
      <div class="brand__square"></div>
      <div class="brand__name">RDP<br>Thermal,<br>Inc.</div>
    </header>

    <section class="headline">
      <p class="headline__lead">TRYING TO ENTER THE</p>
      <p class="headline__key">GEOTHERMAL<br>LOGGING MARKET?</p>
      <span class="headline__rule headline__rule--left"></span>
      <span class="headline__rule headline__rule--right"></span>
    </section>

    <div class="tool tool--horizontal" role="img" aria-label="Photo of a logging tool with bow-spring centralizer, lying horizontally"></div>
    <div class="tool tool--centralizer" role="img" aria-label="Photo of the full, double centralizer logging tool standing upright"></div>
    <div class="tool tool--slim" role="img" aria-label="Photo of a slim metal logging tool standing upright"></div>

    <section class="product">
      <p class="product__name">FULL, DOUBLE</p>
      <p class="product__name product__name--accent">CENTARLIZER</p>
    </section>

    <div class="cta">ASK US</div>
    <p class="cta-copy">about increasing the temperature rating for your existing tools</p>
    <div class="site">rdpthermal.com</div>
  </main>
</body>
</html>
```